I will ask the design of the business card

We are looking for business card design of the new company "VORTELL PAYWORKS STUDIO LLC." Based in Azerbaijan.
In case
We are working on Azerbaijan to set up the first exchange of crypto currencies.

The key currency used in exchanges is called "MIRTA".
In case
We are doing project to make crypto currency infrastructure.

We provide state-of-the-art technology to the world.

```html
<!DOCTYPE html>
<html lang="en">
<head>
<meta charset="utf-8">
<title>Vortell Payworks Studio LLC. — Business Card</title>
<link rel="stylesheet" href="https://fonts.googleapis.com/css2?family=Arimo:ital,wght@0,400;1,400&display=swap">
<style>
  :root {
    --navy: #0f3a63;
    --gold: #e9b325;
    --shadow: #d4d4d4;
    --ink: #333333;
    --paper: #ffffff;
  }
  html, body {
    margin: 0;
    padding: 0;
    width: 955px;
    height: 1200px;
    overflow: hidden;
    background: var(--paper);
  }
  .card-sheet {
    display: block;
    width: 955px;
    height: 1200px;
    font-family: "Arimo", Arial, sans-serif;
  }
  .fill-navy { fill: var(--navy); }
  .fill-gold { fill: var(--gold); }
  .fill-shadow { fill: var(--shadow); }
  .fill-paper { fill: var(--paper); }
  .card-edge { fill: none; stroke: var(--ink); stroke-width: 2; }
  .brand-mark-name { fill: var(--navy); font-size: 20px; }
  .company-name { fill: var(--ink); font-size: 28px; }
  .person-name { fill: var(--gold); font-size: 40px; }
  .person-role { fill: var(--gold); font-size: 30px; }
  .contact-label { fill: var(--paper); font-size: 34px; }
  .name-rule { stroke: var(--paper); stroke-width: 3; }
  .icon-line { fill: none; stroke: var(--paper); stroke-width: 1.6; }
  .slogan { fill: var(--ink); font-size: 40px; font-style: italic; }
</style>
</head>
<body>
<svg class="card-sheet" viewBox="0 0 1054 1324" preserveAspectRatio="none" xmlns="http://www.w3.org/2000/svg" aria-label="Business card front and back">
  <defs>
    <clipPath id="front-clip"><rect x="2" y="2" width="1050" height="648" rx="40"/></clipPath>
    <clipPath id="back-clip"><rect x="2" y="674" width="1050" height="648" rx="40"/></clipPath>
  </defs>

  <!-- Front side -->
  <g class="card-front" clip-path="url(#front-clip)">
    <rect class="fill-paper" x="2" y="2" width="1050" height="648"/>

    <g class="header-band">
      <path class="fill-gold" d="M2 2 H676 V110 Q676 181 600 181 H80 Q2 181 2 100 Z"/>
      <path class="fill-paper" d="M2 2 H682 V100 Q672 168 600 168 H90 Q8 168 2 95 Z"/>
    </g>

    <g class="brand-mark">
      <rect class="fill-navy" x="314" y="25" width="81" height="73"/>
      <text class="brand-mark-name" x="405" y="73">VORTELL</text>
    </g>
    <text class="company-name" x="383" y="142" text-anchor="middle">VORTELL PAYWORKS STUDIO LLC.</text>

    <g class="contact-panel">
      <path class="fill-gold" d="M2 234 H620 Q676 234 682 300 V650 H2 Z"/>
      <path class="fill-navy" d="M2 248 H620 Q682 248 682 310 V650 H2 Z"/>
    </g>

    <text class="person-name" x="294" y="325" text-anchor="middle">NAME</text>
    <line class="name-rule" x1="136" y1="337" x2="458" y2="337"/>
    <text class="person-role" x="296" y="377" text-anchor="middle">manager</text>

    <g class="contact-phone">
      <circle class="icon-line" cx="124" cy="444" r="18"/>
      <path class="fill-paper" d="M116 435 q-2 6 4 13 q7 7 13 5 l2 -3 l-5 -4 l-3 2 q-4 -2 -6 -6 l2 -3 l-4 -5 Z"/>
      <text class="contact-label" x="185" y="465">Phone</text>
    </g>
    <g class="contact-email">
      <rect class="fill-paper" x="102" y="508" width="40" height="28"/>
      <path d="M103 509 L122 525 L141 509 M103 535 L117 521 M141 535 L127 521" fill="none" stroke="var(--navy)" stroke-width="2"/>
      <text class="contact-label" x="183" y="538">Email</text>
    </g>
    <g class="contact-website">
      <circle class="icon-line" cx="119" cy="600" r="16"/>
      <ellipse class="icon-line" cx="119" cy="600" rx="7" ry="16"/>
      <line class="icon-line" x1="119" y1="584" x2="119" y2="616"/>
      <line class="icon-line" x1="103" y1="600" x2="135" y2="600"/>
      <line class="icon-line" x1="106" y1="591" x2="132" y2="591"/>
      <line class="icon-line" x1="106" y1="609" x2="132" y2="609"/>
      <text class="contact-label" x="183" y="614">Website</text>
    </g>

    <g class="side-tab">
      <path class="fill-shadow" d="M1052 48 H1034 Q934 48 934 150 V504 Q934 606 1034 606 H1052 Z"/>
      <path class="fill-gold" d="M1052 48 Q952 48 952 150 V504 Q952 606 1052 606 Z"/>
    </g>
  </g>
  <rect class="card-edge" x="2" y="2" width="1050" height="648" rx="40"/>

  <!-- Back side -->
  <g class="card-back" clip-path="url(#back-clip)">
    <rect class="fill-paper" x="2" y="674" width="1050" height="648"/>
    <g class="side-tab-left">
      <path class="fill-shadow" d="M2 735 H18 Q118 735 118 835 V1190 Q118 1290 18 1290 H2 Z"/>
      <path class="fill-navy" d="M2 735 Q100 735 100 835 V1190 Q100 1290 2 1290 Z"/>
    </g>
    <g class="side-tab-right">
      <path class="fill-shadow" d="M1052 735 H1034 Q934 735 934 835 V1190 Q934 1290 1034 1290 H1052 Z"/>
      <path class="fill-gold" d="M1052 735 Q952 735 952 835 V1190 Q952 1290 1052 1290 Z"/>
    </g>
    <text class="slogan" x="529" y="944" text-anchor="middle">slogan</text>
  </g>
  <rect class="card-edge" x="2" y="674" width="1050" height="648" rx="40"/>
</svg>
</body>
</html>
```